World domination merchandise

We need an illustration to print on a notebook (maybe eventually on other kinds of merchandise). We would like the words "Mes plans de domination mondiale" (which means "my world domination plans") in a calligraphy-like font, with maybe a world map, a globe, a flag... It has to be consistent with the vibe of our company, which is named "La Clairière" (The clearing). We are managing a community of entrepreneurs on a web-platform that is regrouping a forum and an online courses portal. Here are some keywords that represent our brand: vintage (in a modern way, if that makes sense), World War II, 40's/50's, entrepreneurship, web-marketing, community, sodality, collaboration.

I've attached a few image we like for inspiration

```html
<!DOCTYPE html>
<html lang="fr">
<head>
<meta charset="utf-8">
<title>Mes plans de domination mondiale — La Clairière</title>
<link rel="stylesheet" href="https://fonts.googleapis.com/css2?family=Graduate&family=Pinyon+Script&display=swap">
<style>
  :root {
    --kraft: #c9a47f;
    --ink: #0b0b0b;
    --illustration-dark: #1c1a18;
    --illustration-mid: #3a322b;
  }
  * { margin: 0; padding: 0; box-sizing: border-box; }
  html, body {
    width: 1200px;
    height: 1199px;
    overflow: hidden;
    background: var(--kraft);
  }
  .cover {
    position: relative;
    width: 1200px;
    height: 1199px;
    background: var(--kraft);
    color: var(--ink);
    font-family: "Graduate", "Rockwell", serif;
  }
  .title { font-weight: 400; }
  .title-line {
    position: absolute;
    font-size: 84px;
    line-height: 1;
    letter-spacing: 1px;
    text-transform: uppercase;
    white-space: nowrap;
  }
  .title-line--mes { left: 250px; top: 110px; }
  .title-line--de { left: 235px; top: 215px; }
  .title-line--domination { left: 220px; top: 320px; }
  .title-line--mondiale { left: 210px; top: 425px; }

  .bar {
    position: absolute;
    background: var(--ink);
  }
  .bar--mes { left: 800px; top: 130px; width: 170px; height: 52px; }
  .bar--de { left: 400px; top: 232px; width: 570px; height: 52px; }
  .bar--domination { left: 870px; top: 340px; width: 100px; height: 52px; }
  .bar--mondiale { left: 790px; top: 445px; width: 180px; height: 52px; }

  .subtitle-band {
    position: absolute;
    left: 210px;
    top: 515px;
    width: 760px;
    height: 84px;
  }
  .subtitle-band__rule {
    position: absolute;
    left: 0;
    right: 0;
    background: var(--ink);
  }
  .subtitle-band__rule--top { top: 0; height: 8px; }
  .subtitle-band__rule--bottom { bottom: 0; height: 16px; }
  .subtitle-band__text {
    position: absolute;
    left: 0;
    right: 0;
    top: 16px;
    height: 48px;
    text-align: center;
    font-family: "Pinyon Script", cursive;
    font-size: 34px;
    line-height: 48px;
    color: var(--ink);
  }

  .emblem {
    position: absolute;
    left: 0;
    top: 620px;
    width: 1200px;
    height: 360px;
  }
  .emblem__dash {
    position: absolute;
    background: var(--ink);
    height: 30px;
    width: 110px;
  }
  .emblem__dash--left { left: 250px; top: 110px; }
  .emblem__dash--right { left: 840px; top: 200px; }
  .emblem__illustration {
    position: absolute;
    left: 430px;
    top: 0;
    width: 340px;
    height: 350px;
    background: linear-gradient(160deg, var(--illustration-mid), var(--illustration-dark));
  }

  .brand {
    position: absolute;
    left: 0;
    right: 0;
    top: 1030px;
    text-align: center;
  }
  .brand__name {
    font-family: "Graduate", "Rockwell", serif;
    font-size: 96px;
    font-weight: 400;
    line-height: 1;
    color: var(--ink);
    text-transform: uppercase;
    letter-spacing: 2px;
    white-space: nowrap;
  }
</style>
</head>
<body>
  <main class="cover">
    <h1 class="title">
      <span class="title-line title-line--mes">Mes plans</span>
      <span class="title-line title-line--de">de</span>
      <span class="title-line title-line--domination">Domination</span>
      <span class="title-line title-line--mondiale">Mondiale</span>
    </h1>
    <div class="bar bar--mes"></div>
    <div class="bar bar--de"></div>
    <div class="bar bar--domination"></div>
    <div class="bar bar--mondiale"></div>

    <div class="subtitle-band">
      <div class="subtitle-band__rule subtitle-band__rule--top"></div>
      <p class="subtitle-band__text">My World Domination Plans</p>
      <div class="subtitle-band__rule subtitle-band__rule--bottom"></div>
    </div>

    <div class="emblem">
      <div class="emblem__dash emblem__dash--left"></div>
      <div class="emblem__illustration" role="img" aria-label="Illustration : globe terrestre avec un drapeau planté"></div>
      <div class="emblem__dash emblem__dash--right"></div>
    </div>

    <div class="brand">
      <p class="brand__name">La Clairière</p>
    </div>
  </main>
</body>
</html>
```